Personal Business Card

Looking for a clean and modern personal business card. Basically I need something catchy to give to potential clients and people I meet. I do a lot of freelancing (from DJ'ing to wedding videography, but its mostly on the event side of things) so it's more-so about selling myself rather than identifying with a company. I'm starting to meet more people that I want to work with after meeting them so I'm revamping my business cards.

I'm looking for a clean and modern design- I know that's really vague but I'm fine with anything ranging from a symbol to just a fancy version of my name.

Details I need on the front:
Dennis Kowal
dennis@denniskowal-mail.net
(555) 807-2291

On the back I'd like to have something simple like "Nice to have met you today" or "Great meeting you".

UPDATE 9/27 Noon: My apologies for not putting it up before- I'm definitely looking for full color. Doesn't have to be a rainbow but I am looking for the least amount of blank white as possible.

UPDATE 10/1: Really impressed with what I've been getting so far and I'm working on giving everyone feedback- if your design is still up then you're still in the run. Looking for something more unique and modern so please do not post something that looks like a template from Cardloom!

Target Market(s)

Mainly to give to people aged 18-35. Most of my encounters will be casual so the card should have a "young" feeling to it. I rarely do anything in the corporate world so it doesn't have to be boring. It should give the impression that I'm the one they should go to if they need what I do (again it changes every weekend so I'll probably say the "what I do" part.

Industry/Entity Type

Wedding

Requirements
Must have
• Basically the contact information listed above
Nice to have
• I really like the colors Blue, Silver, and Purple. They don't have to necessarily all be there though. I do like the look of polished metal if that makes sense.
Should not have
• A template that resembles card-loom. I'm in a point in my life where I'm working a lot of different markets/areas so the card does not need to have an address or address placeholder.

```html
<!DOCTYPE html>
<html lang="en">
<head>
<meta charset="utf-8">
<title>Dennis Kowal — Business Card</title>
<link rel="stylesheet" href="https://fonts.googleapis.com/css2?family=Barlow:wght@400;500;700;800&display=swap">
<style>
  :root {
    --card-bg: #464a54;
    --mosaic-light: #545964;
    --mosaic-dark: #3a3e47;
    --bubble: rgba(112, 140, 186, 0.78);
    --bubble-ink: #1f4fa3;
    --bubble-ink-light: #e3ebf7;
    --white: #ffffff;
    --silver: #b7bbc3;
    --icon: #6d82a8;
    --monogram-deep: #1d4a9a;
    --monogram-light: #2f7cc4;
  }
  html, body {
    margin: 0;
    padding: 0;
    width: 1200px;
    height: 670px;
    overflow: hidden;
    background: var(--card-bg);
  }
  .card {
    position: relative;
    width: 1200px;
    height: 670px;
    overflow: hidden;
    font-family: "Barlow", "DIN Alternate", sans-serif;
    background: var(--card-bg);
  }
  .mosaic-texture {
    position: absolute;
    inset: 0;
    background:
      radial-gradient(ellipse at 20% 15%, var(--mosaic-light) 0%, transparent 55%),
      radial-gradient(ellipse at 85% 80%, var(--mosaic-light) 0%, transparent 50%),
      linear-gradient(125deg, var(--mosaic-dark) 0%, var(--card-bg) 45%, var(--mosaic-dark) 100%);
  }
  .bubble {
    position: absolute;
    left: 0;
    top: 0;
  }
  .bubble-text {
    position: absolute;
    left: 74px;
    top: 70px;
    margin: 0;
    font-size: 54px;
    line-height: 70px;
    font-weight: 500;
  }
  .bubble-text .line-strong { color: var(--bubble-ink); display: block; }
  .bubble-text .line-soft { color: var(--bubble-ink-light); display: block; }
  .contact {
    position: absolute;
    right: 553px;
    text-align: right;
    margin: 0;
    white-space: nowrap;
    line-height: 1;
  }
  .name {
    top: 326px;
    font-size: 54px;
    font-weight: 800;
    letter-spacing: 1.5px;
    color: var(--white);
  }
  .name .surname { color: var(--silver); }
  .phone {
    top: 398px;
    font-size: 40px;
    font-weight: 700;
    letter-spacing: 1px;
    color: var(--white);
  }
  .email {
    top: 516px;
    font-size: 38px;
    font-weight: 500;
    color: var(--white);
  }
  .website {
    top: 574px;
    font-size: 38px;
    font-weight: 500;
    color: var(--silver);
  }
  .services {
    position: absolute;
    left: 700px;
    top: 200px;
  }
  .monogram-area {
    position: absolute;
    left: 712px;
    top: 330px;
    width: 440px;
    height: 340px;
    background: linear-gradient(100deg, var(--monogram-deep) 0%, var(--monogram-deep) 45%, var(--monogram-light) 55%, var(--monogram-light) 100%);
  }
</style>
</head>
<body>
<main class="card">
  <div class="mosaic-texture" role="img" aria-label="Dark grey pixel mosaic background pattern"></div>

  <svg class="bubble" width="660" height="300" viewBox="0 0 660 300" aria-hidden="true">
    <path d="M62 55 H612 Q621 55 621 64 V230 Q621 239 612 239 H518 L518 292 Q500 262 478 239 H62 Q53 239 53 230 V64 Q53 55 62 55 Z" fill="var(--bubble)"/>
  </svg>
  <p class="bubble-text">
    <span class="line-strong">great to meet you.</span>
    <span class="line-soft">let’s have a chat.</span>
  </p>

  <svg class="services" width="420" height="100" viewBox="0 0 420 100" aria-label="Music, video and production services" role="img">
    <g fill="none" stroke="var(--icon)" stroke-width="11" stroke-linecap="round">
      <path d="M14 66 V50 A45 45 0 0 1 104 50 V66"/>
    </g>
    <g fill="var(--icon)">
      <rect x="4" y="54" width="26" height="42" rx="8"/>
      <rect x="88" y="54" width="26" height="42" rx="8"/>
      <rect x="158" y="6" width="112" height="76"/>
    </g>
    <g fill="var(--card-bg)">
      <rect x="180" y="20" width="68" height="48"/>
      <rect x="163" y="11" width="9" height="9"/><rect x="163" y="31" width="9" height="9"/>
      <rect x="163" y="51" width="9" height="9"/><rect x="163" y="68" width="9" height="9"/>
      <rect x="256" y="11" width="9" height="9"/><rect x="256" y="31" width="9" height="9"/>
      <rect x="256" y="51" width="9" height="9"/><rect x="256" y="68" width="9" height="9"/>
    </g>
    <rect x="297" y="4" width="110" height="96" rx="18" fill="var(--icon)"/>
    <rect x="312" y="20" width="80" height="66" rx="4" fill="var(--card-bg)"/>
    <g fill="var(--icon)">
      <rect x="318" y="26" width="14" height="12"/><rect x="338" y="26" width="14" height="12"/><rect x="358" y="26" width="14" height="12"/><rect x="376" y="26" width="11" height="12"/>
      <rect x="318" y="44" width="14" height="12"/><rect x="338" y="44" width="14" height="12"/><rect x="358" y="44" width="14" height="12"/><rect x="376" y="44" width="11" height="12"/>
      <rect x="318" y="62" width="14" height="18"/><rect x="338" y="62" width="14" height="18"/><rect x="358" y="62" width="14" height="18"/><rect x="376" y="62" width="11" height="18"/>
    </g>
  </svg>

  <div class="monogram-area" role="img" aria-label="Large personal monogram in deep and bright blue, bleeding off the bottom edge"></div>

  <p class="contact name">DENNIS <span class="surname">KOWAL</span></p>
  <p class="contact phone">(555) 807-2291</p>
  <p class="contact email">dennis@denniskowal-mail.net</p>
  <p class="contact website">www.denniskowal-site.net</p>
</main>
</body>
</html>
```